Consulting firm needs a professional letterhead design

We need a professional letterhead design which is simple but unique. It should carry attributes of the latest designs in the market suitable for professional environmental consultancies.

- The logo is attached for you to USE.
- Our preferred color scheme is that shown in the logo.
- Letterhead text color is your choice to make.
- Logo to the left and text to the right plus slogan/tagline is desirable for this letterhead.

Use any address etc. of your choice in the letterhead.

Target Market(s)

Consulting firms and government agencies

Industry/Entity Type

Environmental Consultant

Colors
acd037
fece3e
85cae6
3277b5

Requirements
Must have
• Logo supplied and color scheme must be used.
Nice to have
• Nexa font is used in the Logo, so it would ne nice to have nexa font in the letterhead too.

```html
<!DOCTYPE html>
<html lang="en">
<head>
<meta charset="utf-8">
<title>Terravent Letterhead</title>
<link href="https://fonts.googleapis.com/css2?family=Montserrat:wght@500;700;800&family=Arimo:wght@400;700&display=swap" rel="stylesheet">
<style>
  :root {
    --navy: #2a3046;
    --blue: #3277b5;
    --sky: #85cae6;
    --lime: #acd037;
    --sun: #fece3e;
    --ink: #2b2b2b;
    --muted: #555b66;
    --paper: #ffffff;
    --shade: #eceded;
  }
  * { margin: 0; padding: 0; box-sizing: border-box; }
  html, body { width: 849px; height: 1200px; overflow: hidden; background: var(--paper); }
  .letterhead {
    position: relative;
    width: 849px;
    height: 1200px;
    background: var(--paper);
    font-family: "Arimo", Arial, sans-serif;
    color: var(--ink);
    overflow: hidden;
  }
  .header-band {
    position: absolute;
    left: 300px; top: 52px;
    width: 549px; height: 34px;
    background: var(--navy);
  }
  .brand {
    position: absolute;
    left: 34px; top: 36px;
    width: 256px;
    display: flex;
    align-items: center;
    gap: 12px;
  }
  .brand-dot {
    flex: none;
    width: 50px; height: 50px;
    border-radius: 50%;
    background: var(--blue);
  }
  .brand-text { display: flex; flex-direction: column; }
  .brand-name {
    font-family: "Montserrat", sans-serif;
    font-weight: 800;
    font-size: 26px;
    letter-spacing: 1px;
    color: var(--blue);
    line-height: 1;
  }
  .brand-tagline {
    margin-top: 5px;
    font-family: "Montserrat", sans-serif;
    font-weight: 500;
    font-size: 8.5px;
    color: var(--blue);
    white-space: nowrap;
  }
  .address {
    position: absolute;
    right: 32px; top: 96px;
    display: flex; align-items: center; gap: 6px;
    font-family: "Montserrat", sans-serif;
    font-weight: 700;
    font-size: 13px;
    color: var(--navy);
  }
  .corner-shape {
    position: absolute;
    right: -120px; bottom: -120px;
    width: 420px; height: 420px;
    border-radius: 50%;
    background: radial-gradient(circle at 40% 40%, #f3f4f4, var(--shade));
  }
  .contact {
    position: absolute;
    left: 40px; top: 1068px;
  }
  .contact-title {
    font-weight: 700;
    font-size: 15px;
    color: var(--navy);
    margin-bottom: 12px;
  }
  .contact-list { list-style: none; }
  .contact-item {
    display: flex; align-items: center; gap: 10px;
    font-size: 13px;
    color: var(--muted);
    height: 32px;
  }
  .contact-item svg { width: 14px; height: 14px; fill: var(--navy); }
</style>
</head>
<body>
<div class="letterhead">
  <div class="header-band"></div>

  <div class="brand">
    <span class="brand-dot"></span>
    <div class="brand-text">
      <span class="brand-name">TERRAVENT</span>
      <span class="brand-tagline">Balanced climate and sustainability</span>
    </div>
  </div>

  <div class="address">
    <svg width="12" height="16" viewBox="0 0 12 16" aria-hidden="true"><path fill="#2a3046" d="M6 0C2.7 0 0 2.6 0 5.9 0 10.3 6 16 6 16s6-5.7 6-10.1C12 2.6 9.3 0 6 0zm0 8.2A2.3 2.3 0 1 1 6 3.6a2.3 2.3 0 0 1 0 4.6z"/></svg>
    <span>Unit 48, Greenfield Park, Riverside Lane, Nashik 422011</span>
  </div>

  <div class="corner-shape"></div>

  <section class="contact">
    <h2 class="contact-title">CONTACT INFORMATION</h2>
    <ul class="contact-list">
      <li class="contact-item">
        <svg viewBox="0 0 16 16" aria-hidden="true"><path d="M3.6 1.2 5.9 3.5c.4.4.4 1 0 1.4L4.7 6.1a9 9 0 0 0 5.2 5.2l1.2-1.2c.4-.4 1-.4 1.4 0l2.3 2.3c.4.4.4 1 0 1.4l-1.2 1.2C11 16.6 -.6 5 .8 2.4L2.2 1.2c.4-.4 1-.4 1.4 0z"/></svg>
        <span>: +91 020 4417 390</span>
      </li>
      <li class="contact-item">
        <svg viewBox="0 0 16 16" aria-hidden="true"><path d="M8 0a8 8 0 1 0 4.6 14.5l-.8-1.2A6.5 6.5 0 1 1 14.5 8v.8c0 .9-.6 1.6-1.4 1.6s-1.3-.7-1.3-1.6V4.5h-1.4v.8A3.8 3.8 0 1 0 10.7 11a2.8 2.8 0 0 0 2.4 1.2C14.7 12.2 16 10.8 16 8.8V8a8 8 0 0 0-8-8zm0 10.3A2.3 2.3 0 1 1 8 5.7a2.3 2.3 0 0 1 0 4.6z"/></svg>
        <span>: office@terravent.com</span>
      </li>
      <li class="contact-item">
        <svg viewBox="0 0 16 16" aria-hidden="true"><circle cx="8" cy="8" r="8"/></svg>
        <span>: http://www.terraventgroup.com</span>
      </li>
    </ul>
  </section>
</div>
</body>
</html>
```